Social Media Graphics - ALL TEXT RK

We are looking for a series of social media graphics for Instagram (standard size 1:1 (1080x1080px) that are ALL TEXT. We want the following quotes below on each graphic; one quote per graphic. AND, In very small letters at the bottom of each graphic, add @RKMarlowLive

The look and feel of these graphics should be complimentary to the color palette attached below; but keep them simple. But the design is up to you; at the end of this document, I provided various samples of all text graphics that I like as examples.

Target Market(s)

women looking to lose weight

Industry/Entity Type

health and wellness

Colors
E54698
E96AAD
F1A4CE
F9D9EA
FCEFF6

Requirements
Must have
• the quotes in the document
Should not have
• no stock photography

```html
<!DOCTYPE html>
<html lang="en">
<head>
<meta charset="utf-8">
<title>Overnight Remedy Quote</title>
<link href="https://fonts.googleapis.com/css2?family=Montserrat:wght@400;900&display=swap" rel="stylesheet">
<style>
  :root {
    --magenta-deep: #d01a68;
    --magenta-mid: #e0468e;
    --pink-glow: #ef6eab;
    --blush: #f1a4ce;
    --petal: #f9d9ea;
    --white: #ffffff;
    --handle: #f6d7ea;
  }
  html, body { margin: 0; padding: 0; overflow: hidden; }
  .post {
    position: relative;
    width: 1200px;
    height: 1200px;
    overflow: hidden;
    background: radial-gradient(circle at 50% 49%, var(--pink-glow) 0%, var(--magenta-mid) 38%, var(--magenta-deep) 75%);
    font-family: "Montserrat", sans-serif;
  }
  .backdrop { position: absolute; inset: 0; width: 1200px; height: 1200px; }
  .quote {
    position: absolute;
    left: 206px;
    top: 266px;
    margin: 0;
    color: var(--white);
    font-size: 89px;
    line-height: 97px;
    font-weight: 400;
    text-transform: uppercase;
    letter-spacing: 0.5px;
  }
  .quote strong { font-weight: 900; }
  .handle {
    position: absolute;
    left: 208px;
    top: 1075px;
    margin: 0;
    color: var(--handle);
    font-size: 35px;
    font-weight: 400;
  }
</style>
</head>
<body>
<div class="post">
  <svg class="backdrop" viewBox="0 0 1200 1200" aria-hidden="true">
    <defs>
      <radialGradient id="soft-orb">
        <stop offset="0" stop-color="var(--blush)" stop-opacity="0.35"/>
        <stop offset="1" stop-color="var(--blush)" stop-opacity="0"/>
      </radialGradient>
    </defs>
    <circle class="orb" cx="1080" cy="140" r="260" fill="url(#soft-orb)"/>
    <circle class="orb" cx="110" cy="1080" r="240" fill="url(#soft-orb)"/>
    <rect class="frame" x="40" y="40" width="1120" height="1120" rx="28" fill="none" stroke="var(--petal)" stroke-opacity="0.45" stroke-width="2"/>
    <rect class="accent-bar" x="208" y="226" width="120" height="8" rx="4" fill="var(--petal)" fill-opacity="0.8"/>
    <rect class="accent-bar" x="872" y="1092" width="120" height="8" rx="4" fill="var(--petal)" fill-opacity="0.5"/>
  </svg>
  <p class="quote">Wake up<br><strong>tomorrow</strong><br>with a flatter<br><strong>belly- yes,</strong><br>this overnight<br>remedy works<br>like <strong>magic!</strong></p>
  <p class="handle">@RKMarlowLive</p>
</div>
</body>
</html>
```